AWESOME RETAILER OF PHONE ACCESSORIES NEEDS AWESOME WEBSITE FROM AWESOME DESIGNER

We currently do not have any website and are looking for one for our new store. We are a retailer who sells novaphone accessories, speakers, electronics, cables with the best pricing guaranteed. We carry all top name brands including:

TrailGuard : http://www.trailguard-cases.example/en/

Ferncase : http://www.ferncase.example/

Quindle : http://www.quindle.example/Default.asp

Varenta : http://www.varenta.example/

Bold Kit : http://www.bold-kit.example/

http://www.glintshield.example/hot-sellers/handset-5-frost-white.html

http://www.tamsel-works.example/products/detail.cfm?prodID=2

http://vostrek.example/

http://www.plimm.example/

We would like to see our logo's used and a website that is trendy and catchy to our demographics. Our demographic is male/female between the ages of 16-45.

Target Market(s)

Male/Femal Ages -16-45

Industry/Entity Type

Electronics

Requirements
Must have
• Must use our logo's and be a catchy fun website keeps the customers eye.
Coupon Tab where customers can print coupons
Products Tab where we can display all of our brands of products
Contact us page
Location Page
CHATTERLY/BLURTLY ACCOUNT TO BE LINKED TO SITE
WEBSITE WILL BE HOSTED BY HOSTWREN.EXAMPLE PLEASE MAKE SURE YOUR DESIGN IS COMPATIBLE WITH THEM.

PLEASE BE SURE TO USE OUR LOGO IN YOUR DESIGN YOU SUBMIT, THEY ARE ATTACHED TO THIS PROJECT
Nice to have
• We would like a slot where a video can be posted from clipvane
Authorized dealer banner
Should not have
• not a dark website but bright and vibrant
Do not use any logos or images that are trademarked by Quorral.

```html
<!DOCTYPE html>
<html lang="en">
<head>
<meta charset="utf-8">
<title>Cellvio – novaphone accessories</title>
<link href="https://fonts.googleapis.com/css2?family=Arimo:wght@400;700&family=Oswald:wght@500;600&family=Archivo:wght@800&family=Quicksand:wght@300;400&display=swap" rel="stylesheet">
<style>
:root{
  --green:#76b043;
  --green-dark:#5f9634;
  --dark:#414141;
  --ink:#2b2b2b;
  --text:#555;
  --white:#fff;
}
*{box-sizing:border-box;margin:0;padding:0}
html,body{width:1026px;height:1200px;overflow:hidden;background:var(--white)}
body{position:relative;font-family:Arimo,Arial,sans-serif;color:var(--text)}
.abs{position:absolute}

/* top bar */
.topbar{left:0;top:0;width:1026px;height:30px;border-bottom:1px solid #e2e2e2;background:#fafafa}
.social{left:96px;top:11px;display:flex;gap:8px;font-size:7.5px;font-weight:700;color:#555;line-height:8px}
.social span+span{border-left:1px solid #999;padding-left:8px}
.utility{right:96px;top:12px;display:flex;font-size:7px;color:#333}
.utility span{padding:0 8px;border-left:1px solid #333;line-height:7px}
.utility span:first-child{border:0}
.utility span:last-child{padding-right:0}

/* header */
.brand{left:96px;top:98px;font-family:Arimo,Arial,sans-serif;font-size:26px;font-weight:700;color:var(--ink);line-height:30px}
.cat-nav{left:194px;top:101px;display:flex;height:36px;align-items:center}
.cat-nav a{font-family:Quicksand,sans-serif;font-size:18px;color:var(--ink);text-decoration:none;padding:0 15px;border-left:1px solid #bbb;line-height:36px}
.cat-nav a:first-child{border:0;padding-left:0}
.search{left:760px;top:110px;width:168px;height:22px;border:1px solid #999;font-size:7px;color:#333;padding:7px 8px}
.search svg{position:absolute;right:5px;top:3px}

/* nav */
.mainnav{left:0;top:153px;width:1026px;height:23px;background:linear-gradient(#84bd4c,var(--green-dark))}
.home-tab{left:95px;top:150px;width:67px;height:29px;background:var(--white);box-shadow:0 1px 3px rgba(0,0,0,.3);font-size:8.5px;font-weight:700;color:#111;text-align:center;line-height:29px}
.mainnav ul{position:absolute;left:182px;top:8px;display:flex;list-style:none;font-size:8.5px;font-weight:700;color:var(--white)}
.mainnav li{padding:0 10px;border-left:1px solid rgba(255,255,255,.7);line-height:8px}
.mainnav li:first-child{border:0;padding-left:0}

/* hero */
.hero-band{left:0;top:176px;width:1026px;height:252px;background:var(--dark)}
.content-band{left:0;top:428px;width:1026px;height:297px;background:linear-gradient(#e9e9e9,#f2f2f2)}
.slider{left:96px;top:205px;width:831px;height:303px;background:var(--white);box-shadow:0 12px 22px -10px rgba(0,0,0,.35)}
.cap-main{left:92px;top:303px;height:42px;padding:0 14px 0 23px;background:var(--ink);color:var(--white);font-family:Oswald,sans-serif;font-weight:600;font-size:20px;line-height:42px}
.cap-sub{left:92px;top:345px;height:36px;padding:0 16px 0 23px;background:var(--green);color:var(--white);font-family:Archivo,sans-serif;font-weight:800;font-size:15px;line-height:36px}
.dots{left:115px;top:480px;display:flex;gap:6px}
.dots i{width:9px;height:9px;background:#444}
.dots i.on{background:var(--green)}
.hero-photo{left:545px;top:235px;width:355px;height:245px;border-radius:6px;background:radial-gradient(ellipse at center,#8a8a8a 0%,#3a3a3a 55%,#fff 72%)}

/* category columns */
.col{top:543px;width:190px}
.col h3{font-family:Quicksand,sans-serif;font-weight:400;font-size:17px;color:var(--ink);margin-bottom:10px;line-height:20px}
.col h4{font-family:Archivo,sans-serif;font-weight:800;font-size:12px;line-height:12.5px;color:var(--ink)}
.col h4 em{font-style:normal;color:var(--green)}
.col p{margin-top:10px;font-size:7.9px;line-height:9.9px;letter-spacing:.25px;white-space:nowrap;color:#555}
.col .more{display:inline-block;margin-top:16px;background:var(--green);color:var(--white);font-size:8.5px;padding:2px 5px}
.sep{top:542px;width:1px;height:158px;background:#bdbdbd}

/* services */
.services{left:96px;top:755px;width:840px}
.services h2{font-family:Archivo,sans-serif;font-weight:800;font-size:14.5px;color:var(--ink);margin-bottom:5px}
.services p{font-size:9.6px;line-height:11.5px;height:172px;overflow:hidden;text-align:justify;color:#555}

/* footer */
.footer{left:0;top:972px;width:1026px;height:203px;background:var(--dark)}
.fsep{top:1014px;width:1px;height:116px;background:#777}
.deliv{left:100px;top:1042px;font-size:11px;color:var(--white)}
.free{left:97px;top:1050px;font-family:Quicksand,sans-serif;font-weight:300;font-size:46px;line-height:52px;color:var(--green);letter-spacing:1px}
.fhead{font-size:14px;color:var(--green)}
.tweet{display:flex;gap:10px;font-size:9.5px;line-height:11.5px}
.tweet .mark{width:13px;height:13px;border:2px solid var(--green);flex:none;margin-top:2px}
.tweet a{color:var(--green);text-decoration:none}
.ago{font-size:6.5px;text-align:right;margin:6px 0 15px}
.contact-row{display:flex;gap:8px;align-items:flex-start;font-size:9.5px;line-height:10px;margin-top:11px}
.email{width:160px;height:26px;background:var(--white);color:#333;font-size:9.5px;padding:8px 7px}
.subscribe{width:71px;height:21px;background:var(--green);font-size:9.5px;padding:5px 7px;margin-top:12px}
.copyright{left:0;top:1175px;width:1026px;height:25px;background:var(--green);color:var(--white);font-size:9.5px;text-align:center;line-height:25px}
</style>
</head>
<body>

<div class="abs topbar"></div>
<div class="abs social"><span>CHATTERLY</span><span>BLURTLY</span><span>Linkvale</span></div>
<div class="abs utility"><span>SHOP</span><span>MY ACCOUNT</span><span>CHECKOUT</span><span>LOCATION</span></div>

<div class="abs brand">Cellvio</div>
<nav class="abs cat-nav">
  <a href="#">cables</a><a href="#">phone cases</a><a href="#">speakers</a><a href="#">electronics</a>
</nav>
<div class="abs search">SEARCH
  <svg width="14" height="14" viewBox="0 0 14 14"><circle cx="6" cy="6" r="4.5" fill="none" stroke="#76b043" stroke-width="1.3"/><line x1="9.2" y1="9.2" x2="13" y2="13" stroke="#76b043" stroke-width="1.5"/></svg>
</div>

<div class="abs mainnav">
  <ul><li>ABOUT US</li><li>PRODUCTS</li><li>COUPON</li><li>CONTACT US</li></ul>
</div>
<div class="abs home-tab">HOME</div>

<div class="abs hero-band"></div>
<div class="abs content-band"></div>
<section class="abs slider"></section>
<div class="abs hero-photo" role="img" aria-label="Disassembled novaphone with its parts laid out: back panel, frame, battery, board and front screen"></div>
<div class="abs cap-main">NOVAPHONE SPEAKERS RELATED TEXT HERE</div>
<div class="abs cap-sub">SOME TEXT HERE ABOUT NOVAPHONE SPEAKERS</div>
<div class="abs dots"><i></i><i></i><i class="on"></i><i></i><i></i></div>

<article class="abs col" style="left:96px">
  <h3>cables</h3>
  <h4>HEADING OF<br><em>NOVAPHONE</em> CABLES</h4>
  <p>Some text here Some text here Some<br>Some text here Some text here Some<br>Some text here Some text here Some<br>Some text here Some text here Some<br>Some text here Some text here Some<br>Some text here Some text here Some</p>
  <span class="more">Read More</span>
</article>
<div class="abs sep" style="left:283px"></div>
<article class="abs col" style="left:329px">
  <h3>phone cases</h3>
  <h4>HEADING OF<br><em>NOVAPHONE</em> CASES</h4>
  <p>Some text here Some text here Some<br>Some text here Some text here Some<br>Some text here Some text here Some<br>Some text here Some text here Some<br>Some text here Some text here Some<br>Some text here Some text here Some</p>
  <span class="more">Read More</span>
</article>
<div class="abs sep" style="left:516px"></div>
<article class="abs col" style="left:561px">
  <h3>speakers</h3>
  <h4>HEADING OF<br><em>NOVAPHONE</em> SPEAKERS</h4>
  <p>Some text here Some text here Some<br>Some text here Some text here Some<br>Some text here Some text here Some<br>Some text here Some text here Some<br>Some text here Some text here Some<br>Some text here Some text here Some</p>
  <span class="more">Read More</span>
</article>
<div class="abs sep" style="left:742px"></div>
<article class="abs col" style="left:784px">
  <h3>electronics</h3>
  <h4>HEADING OF<br><em>NOVAPHONE</em> CABLES</h4>
  <p>Some text here Some text here Some<br>Some text here Some text here Some<br>Some text here Some text here Some<br>Some text here Some text here Some<br>Some text here Some text here Some<br>Some text here Some text here Some</p>
  <span class="more">Read More</span>
</article>

<section class="abs services">
  <h2>YOUR SERVICES RELATED TEXT HERE</h2>
  <p>Some text here Some text here Some Some text here Some text here Some Some text here Some text here Some Some text here Some text here Some Some text here Some text here Some Some text here Some text here Some Some text here Some text here Some Some text here Some text here Some Some text here Some text here Some Some text here Some text here Some Some text here Some text here Some Some text here Some text here Some Some text here Some text here Some Some text here Some text here Some Some text here Some text here Some Some text here Some text here Some Some text here Some text here Some Some text here Some text here Some Some text here Some text here Some Some text here Some text here Some Some text here Some text here Some Some text here Some text here Some Some text here Some text here Some Some text here Some text here Some Some text here Some text here Some Some text here Some text here Some Some text here Some text here Some Some text here Some text here Some Some text here Some text here Some Some text here Some text here Some Some text here Some text here Some Some text here Some text here Some Some text here Some text here Some Some text here Some text here Some Some text here Some text here Some Some text here Some text here Some Some text here Some text here Some Some text here Some text here Some Some text here Some text here Some Some text here Some text here Some Some text here Some text here Some Some text here Some text here Some Some text here Some text here Some Some text here Some text here Some Some text here Some text here Some Some text here Some text here Some Some text here Some text here Some Some text here Some text here Some Some text here Some text here Some Some text here Some text here Some Some text here Some text here Some Some text here Some text here Some Some text here Some text here Some Some text here Some text here Some Some text here Some text here Some Some text here Some text here Some Some text here Some text here Some Some text here Some text here Some Some text here Some text here Some Some text here Some text here Some Some text here Some text here Some Some text here Some text here Some Some text here Some text here Some Some text here Some text here Some Some text here Some text here Some Some text here Some text here Some Some text here Some text here Some Some text here Some text here Some Some text here Some text here Some Some text here Some text here Some Some text here Some text here Some Some text here Some text here Some Some text here Some text here Some Some text here Some text here Some Some text here Some text here Some Some text here Some text here Some Some text here Some text here Some Some text here Some text here Some Some text here Some text here Some Some text here Some text here Some Some text here Some text here Some Some text here Some text here Some Some text here Some text here Some Some text here Some text here Some Some text here Some text here Some Some text here Some text here Some Some text here Some text here Some Some text here Some text here Some Some text here Some text here Some Some text here Some text here Some Some text here Some text here Some Some text here Some text here Some Some text here Some text here Some Some text here Some text here Some Some text here Some text here Some Some text here Some text here Some Some text here Some text here Some Some text here Some text here Some Some text here Some text here Some Some text here Some text here Some Some text here Some text here Some Some text here Some text here Some Some text here Some text here Some Some text here Some text here Some Some text here Some text here Some Some text here Some text here Some Some text here Some text here Some Some text here Some text here Some Some text here Some text here Some Some text here Some text here Some Some text here Some text here Some Some text here Some text here Some Some text here Some text here Some Some text here Some text here Some Some text here Some text here Some Some text here Some text here Some Some text here Some text here Some Some text here Some text here Some Some text here Some text here Some Some text here Some text here Some Some text here Some text here Some Some text here Some text here Some Some text here Some text here Some Some text here Some text here Some Some text here Some text here Some Some text here Some text here Some Some text here Some text here Some Some text here Some text here Some Some text here Some text here Some Some text here Some text here Some</p>
</section>

<footer class="abs footer"></footer>
<div class="abs fsep" style="left:245px"></div>
<div class="abs fsep" style="left:500px"></div>
<div class="abs fsep" style="left:714px"></div>

<div class="abs deliv">All our deliveries are</div>
<div class="abs free">FREE</div>

<div class="abs" style="left:280px;top:1008px;width:180px;color:#fff">
  <div class="fhead" style="margin-bottom:8px">Recet Tweets</div>
  <div class="tweet"><span class="mark"></span><div>“Some text herre<br>Some text herre Some text herre”<br><a href="#">(http://lnk.example/oPREu3FqJg</a></div></div>
  <div class="ago">10 min ago</div>
  <div class="tweet"><span class="mark"></span><div>“Some text herre<br>Some text herre Some text herre”<br><a href="#">(http://lnk.example/oPREu3FqJg</a></div></div>
</div>

<div class="abs" style="left:531px;top:1022px;width:170px;color:#fff">
  <div class="fhead" style="margin-bottom:4px">Contact us</div>
  <div class="contact-row"><svg width="14" height="12" viewBox="0 0 14 12"><path d="M3 1l2 2.5-1.2 1.3c.8 1.6 2 2.8 3.6 3.6L8.7 7.2 11.2 9 10 11C6 11 1 6 1 2z" fill="#76b043"/></svg><span>123 45 678900</span></div>
  <div class="contact-row"><svg width="14" height="12" viewBox="0 0 14 12"><rect x="1" y="2" width="12" height="8" fill="#76b043"/><path d="M1 2l6 5 6-5" fill="none" stroke="#414141" stroke-width="1"/></svg><span>info@cellvio.example</span></div>
  <div class="contact-row"><svg width="14" height="16" viewBox="0 0 14 16"><circle cx="7" cy="8" r="6" fill="#76b043"/><circle cx="7" cy="8" r="2" fill="#414141"/><rect x="6" y="0" width="2" height="3" fill="#76b043"/></svg><span>Your adress here Your adress<br>here Your adress here</span></div>
</div>

<div class="abs" style="left:756px;top:1026px;color:#fff">
  <div class="fhead" style="margin-bottom:10px">Sign up for our Newsletter</div>
  <div class="email">Email address</div>
  <div class="subscribe">Subscribe</div>
</div>

<div class="abs copyright">Copyright 2013 novaphone accessories &nbsp;I&nbsp; AllRights Reserved &nbsp;I&nbsp; Leader in novaphone accessories</div>

</body>
</html>
```